Business Card Design - Carrington Hill Lodge

We are looking at a new design for our business cards that has a modern and professional look. We run a residential aged care facility focussing on the care of residents. The cards will be used for potential clients, consultants and business opportunities in this sector. Blue and white is our main colours and would to see these colours incorporated in the design.
Industry/Entity Type
Business
Contact Information for Business Card
Carrington Hill Lodge, Darren Pelham, dpelham@carringtonhilllodge.com.au, Finance Manager, 0491 736 208, BCom, 48 Yarrabee Way, Wattle Grove, Qld 4127.

```html
<!DOCTYPE html>
<html lang="en">
<head>
<meta charset="utf-8">
<title>Carrington Hill Lodge – Business Card</title>
<link rel="stylesheet" href="https://fonts.googleapis.com/css2?family=Open+Sans:wght@400;600;800&display=swap">
<style>
  :root {
    --navy: #1f3e4e;
    --steel: #4d7f9c;
    --white: #ffffff;
    --rule: #c9c9c9;
    --backdrop: #e6e7e8;
  }
  * { margin: 0; padding: 0; box-sizing: border-box; }
  html, body { width: 1200px; height: 900px; overflow: hidden; }
  body {
    background: var(--backdrop);
    font-family: "Open Sans", Arial, sans-serif;
    position: relative;
  }
  .card {
    position: absolute;
    left: 300px;
    width: 600px;
    height: 343px;
    border-radius: 22px;
    overflow: hidden;
    box-shadow: 0 6px 18px rgba(0,0,0,.18);
  }
  .card--back { top: 60px; background: var(--navy); }
  .card--front { top: 497px; background: var(--white); }

  .brand {
    position: absolute;
    left: 0; right: 0;
    display: flex;
    justify-content: center;
    align-items: center;
    gap: 12px;
  }
  .brand__dot { width: 18px; height: 18px; border-radius: 50%; background: var(--steel); }
  .brand__name {
    font-weight: 600;
    letter-spacing: 2px;
    text-transform: uppercase;
    font-size: 25px;
    line-height: 1;
  }

  .card--back .brand { top: 158px; }
  .card--back .brand__name { color: var(--white); }

  .card--front .brand { top: 82px; }
  .card--front .brand__name { color: var(--navy); font-size: 22px; }

  .person {
    position: absolute;
    top: 148px; left: 0; right: 0;
    text-align: center;
  }
  .person__name {
    color: var(--navy);
    font-weight: 800;
    font-size: 22px;
    letter-spacing: .5px;
    text-transform: uppercase;
    line-height: 1.2;
  }
  .person__role {
    color: var(--steel);
    font-size: 12.5px;
    text-transform: uppercase;
    letter-spacing: .3px;
  }

  .contact-band {
    position: absolute;
    left: 0; right: 0; bottom: 0;
    height: 112px;
    background: var(--navy);
    border-top: 5px solid var(--rule);
    color: var(--white);
    font-size: 13.5px;
  }
  .contact-band__reach {
    position: absolute;
    left: 28px; bottom: 20px;
    list-style: none;
  }
  .contact-band__reach li { display: flex; align-items: center; gap: 8px; line-height: 22px; }
  .contact-band__reach svg { width: 13px; height: 13px; }
  .contact-band__address {
    position: absolute;
    right: 28px; top: 18px;
    text-align: right;
    font-style: normal;
    line-height: 20px;
  }
</style>
</head>
<body>

<section class="card card--back" aria-label="Card back">
  <div class="brand">
    <span class="brand__dot"></span>
    <span class="brand__name">Carrington Hill Lodge</span>
  </div>
</section>

<section class="card card--front" aria-label="Card front">
  <div class="brand">
    <span class="brand__dot"></span>
    <span class="brand__name">Carrington Hill Lodge</span>
  </div>

  <div class="person">
    <p class="person__name">Darren Pelham</p>
    <p class="person__role">Finance Manager (BCom)</p>
  </div>

  <div class="contact-band">
    <ul class="contact-band__reach">
      <li>
        <svg viewBox="0 0 24 24" fill="none" stroke="currentColor" stroke-width="2.2" aria-hidden="true">
          <path d="M5 3h4l2 5-2.5 1.5a11 11 0 0 0 6 6L16 13l5 2v4a2 2 0 0 1-2 2A17 17 0 0 1 3 5a2 2 0 0 1 2-2z"/>
        </svg>
        0491 736 208
      </li>
      <li>
        <svg viewBox="0 0 24 24" fill="none" stroke="currentColor" stroke-width="2.2" aria-hidden="true">
          <rect x="3" y="5" width="18" height="14" rx="1"/>
          <path d="M3 6l9 7 9-7"/>
        </svg>
        dpelham@carringtonhilllodge.com.au
      </li>
    </ul>
    <address class="contact-band__address">
      48 Yarrabee Way<br>
      Wattle Grove, Qld 4127
    </address>
  </div>
</section>

</body>
</html>
```